Business Card Design Project

I am a psychotherapist, counselor and expressive arts therapist (means I use every art form imaginable in the service of healing). I'm just starting out in private practice in San Francisco, CA. I work with individual adults, children and families. I'd like the card to mirror the simplicity and color palate of my website. I also would love if there is a symbol, image of fire, flame or spark (that is warming, not frightening).

Check out my website: www.lorabecketmft.com

I want the cards to be printed in letter press so please keep that in mind!

Target Market(s)

Upper Middle Class Adults who are progressively minded, artistic or artists, open to psychotherapy, interested in health & healing.

Industry/Entity Type

Business

Requirements
Must have
• Text to be included:

Lora Becket
Counseling, Psychotherapy & Expressive Arts

2914 Alderwood Avenue, Suite D
San Francisco, CA 94127
p. 415.206.3791
lorajanebecket@meadowpost.net

www.lorabecketmft.com

MFT License Number 48671

It's OK to abbreviate Number to # or Street to St., etc.

Must be compatible with letter press printing.
Nice to have
• I don't have a logo. I don't expect designers to necessarily create one for me, but if someone comes up with a simple image (see above about flame), that would be great. I don't have much of a budget now, but expect that to change in the next year or so and then could buy a logo for my website, future letterhead, etc.

```html
<!DOCTYPE html>
<html lang="en">
<head>
<meta charset="utf-8">
<title>Lora Becket – Business Cards</title>
<link rel="stylesheet" href="https://fonts.googleapis.com/css2?family=Federo&family=Didact+Gothic&display=swap">
<style>
  :root {
    --backdrop: #d9d9db;
    --card-paper: #f1f1f1;
    --ink-red: #d9271d;
    --ink-red-soft: #f0a59f;
    --ink-dark: #2f2f2f;
    --card-shadow: rgba(0, 0, 0, 0.18);
  }
  * { box-sizing: border-box; margin: 0; padding: 0; }
  html, body {
    width: 1200px;
    height: 900px;
    overflow: hidden;
  }
  body {
    background: var(--backdrop);
    font-family: "Didact Gothic", "Century Gothic", sans-serif;
    color: var(--ink-dark);
  }
  .canvas {
    position: relative;
    width: 1200px;
    height: 900px;
    display: flex;
    justify-content: center;
    align-items: center;
    gap: 60px;
  }
  .card {
    position: relative;
    width: 340px;
    height: 580px;
    background: var(--card-paper);
    box-shadow: 0 6px 18px var(--card-shadow);
    overflow: hidden;
    text-align: center;
  }
  .card__name {
    font-family: "Federo", "Poiret One", sans-serif;
    font-weight: 400;
    color: var(--ink-red);
    text-transform: uppercase;
    letter-spacing: 1px;
    line-height: 1.15;
  }
  .card__tagline {
    font-size: 14px;
    line-height: 1.25;
  }

  /* Info side */
  .card--info .ornament {
    position: absolute;
    left: 70px;
    top: 140px;
    width: 200px;
    height: 150px;
    border-radius: 50% 50% 40% 40% / 60% 60% 40% 40%;
    background: radial-gradient(ellipse at 50% 60%, var(--ink-red) 0%, var(--ink-red-soft) 60%, transparent 75%);
  }
  .card--info .card__body {
    position: absolute;
    left: 0;
    right: 0;
    top: 310px;
  }
  .card--info .card__name { font-size: 26px; }
  .card--info .card__tagline { margin-top: 6px; }
  .contact {
    margin-top: 20px;
    font-size: 16px;
    line-height: 1.3;
  }
  .address {
    margin-top: 20px;
    font-size: 16px;
    line-height: 1.3;
    font-style: normal;
  }
  .license {
    margin-top: 34px;
    font-size: 14px;
    line-height: 1.25;
  }

  /* Name side */
  .card--name .ornament {
    position: absolute;
    left: -20px;
    top: -20px;
    width: 380px;
    height: 420px;
    background: radial-gradient(ellipse at 60% 40%, var(--ink-red) 0%, var(--ink-red-soft) 55%, transparent 72%);
  }
  .card--name .card__body {
    position: absolute;
    left: 0;
    right: 0;
    top: 420px;
  }
  .card--name .card__name { font-size: 38px; }
  .card--name .card__tagline { margin-top: 8px; }
  .website {
    margin-top: 24px;
    font-size: 15px;
  }
</style>
</head>
<body>
  <main class="canvas">
    <section class="card card--info">
      <div class="ornament" role="img" aria-label="Red swirling flame flourish, letterpress printed"></div>
      <div class="card__body">
        <h2 class="card__name">Lora Becket</h2>
        <p class="card__tagline">Counseling, Psychotherapy &amp; Expressive Arts</p>
        <p class="contact">lorajanebecket@meadowpost.net<br>p. 415.206.3791</p>
        <address class="address">2914 Alderwood Avenue, Suite D<br>San Francisco, CA 94127</address>
        <p class="license">MFT License Number 48671</p>
      </div>
    </section>

    <section class="card card--name">
      <div class="ornament" role="img" aria-label="Large red swirling flame flourish bleeding off the card edges"></div>
      <div class="card__body">
        <h1 class="card__name">Lora Becket</h1>
        <p class="card__tagline">Counseling, Psychotherapy &amp; Expressive Arts</p>
        <p class="website">www.lorabecketmft.com</p>
      </div>
    </section>
  </main>
</body>
</html>
```